Real Estate - Large Sign Design

I am looking for a fresh new look for our leasing signs that will be showcase in front of commercial buildings available for lease. The sign dimension can be either 8'x4' or 4'x8'. They must exemplify our brand (see attachments) and be very visible by people driving by at high speeds.
They must include the following:
- Our logo (vector attached)
- Office Space Available
- 555-018-3274
- Nell Ruby
- Carl Ivey
- www.vantorile.com
Please let me know if you have any questions.
Target Market(s)
Drivers in high traffic areas, walking crowds
Industry/Entity Type
Real Estate
Requirements
Must have
- They must include the following:
- - Our logo (vector attached)
- - Office Space Available
- - 555-018-3274
- - Nell Ruby
- - Carl Ivey
- - www.vantorile.com
Should not have
- Should not be busy or hard to read.

```html
<!DOCTYPE html>
<html lang="en">
<head>
<meta charset="utf-8">
<title>Lease Sign – Office Space Available</title>
<link rel="stylesheet" href="https://fonts.googleapis.com/css2?family=Saira:ital,wght@0,400;0,600;0,700;1,500;1,600;1,700&display=swap">
<style>
  :root {
    --ink: #34343f;
    --white: #ffffff;
    --lime: #6cb52f;
    --green: #0f9f45;
    --green-deep: #14923f;
    --teal: #2f7c66;
    --teal-deep: #25644f;
    --backdrop: #eceeec;
    --label: #6b6f6c;
  }
  * { box-sizing: border-box; margin: 0; padding: 0; }
  html, body { width: 1200px; height: 875px; overflow: hidden; }
  body {
    background: var(--backdrop);
    font-family: "Saira", "Arial Narrow", sans-serif;
    position: relative;
  }
  .sign {
    position: absolute;
    background: var(--white);
    overflow: hidden;
    box-shadow: 0 6px 18px rgba(0,0,0,0.15);
  }
  .sign__shapes { position: absolute; inset: 0; width: 100%; height: 100%; }
  .sign__text { position: absolute; white-space: nowrap; line-height: 1; }
  .sign__lease { color: var(--ink); font-weight: 700; font-style: italic; }
  .sign__offer { color: var(--green); font-weight: 600; font-style: italic; }
  .sign__offer--top { color: var(--lime); }
  .sign__contact { color: var(--ink); font-weight: 500; font-style: italic; }
  .sign__url { color: var(--white); font-weight: 700; font-style: italic; }
  .sign__brand {
    color: var(--white); font-weight: 400; text-transform: uppercase;
    line-height: 1.02; letter-spacing: 0.02em;
  }
  .size-label {
    position: absolute; color: var(--label); font-size: 22px; font-weight: 400;
    text-align: center;
  }

  /* 8' x 4' landscape */
  .sign--wide { left: 60px; top: 300px; width: 470px; height: 395px; }
  .sign--wide .sign__lease { left: 8.5%; top: 6.5%; font-size: 50px; }
  .sign--wide .sign__offer--top { left: 8.5%; top: 22.5%; font-size: 45px; }
  .sign--wide .sign__offer--bottom { left: 8.5%; top: 37.5%; font-size: 45px; }
  .sign--wide .sign__contact--one { left: 8.5%; top: 54%; font-size: 19px; }
  .sign--wide .sign__contact--two { left: 8.5%; top: 61.5%; font-size: 19px; }
  .sign--wide .sign__url { left: 20%; top: 87%; font-size: 21px; }
  .sign--wide .sign__brand { right: 4%; top: 79%; font-size: 15px; text-align: right; }

  /* 4' x 8' upright */
  .sign--tall { left: 630px; top: 80px; width: 520px; height: 610px; }
  .sign--tall .sign__lease { left: 5.5%; top: 11%; font-size: 64px; }
  .sign--tall .sign__offer--top { left: 5.5%; top: 25%; font-size: 60px; }
  .sign--tall .sign__offer--bottom { left: 5.5%; top: 37.5%; font-size: 60px; }
  .sign--tall .sign__contact--one { left: 5.5%; top: 53.5%; font-size: 25px; }
  .sign--tall .sign__contact--two { left: 5.5%; top: 60%; font-size: 25px; }
  .sign--tall .sign__url { left: 7%; top: 88%; font-size: 28px; }
  .sign--tall .sign__brand { right: 4%; top: 84%; font-size: 19px; text-align: right; }

  .size-label--wide { left: 60px; top: 712px; width: 470px; }
  .size-label--tall { left: 630px; top: 707px; width: 520px; }
</style>
</head>
<body>

<section class="sign sign--wide" aria-label="Landscape lease sign">
  <svg class="sign__shapes" viewBox="0 0 100 100" preserveAspectRatio="none" aria-hidden="true">
    <defs>
      <linearGradient id="bandWide" x1="0" y1="0" x2="0" y2="1">
        <stop offset="0" stop-color="#6cb52f"/>
        <stop offset="0.7" stop-color="#0f9f45"/>
      </linearGradient>
    </defs>
    <polygon points="85,0 100,0 100,100 67,100" fill="url(#bandWide)"/>
    <polygon points="0,86 71,76 67,100 0,100" fill="#2f7c66"/>
    <polygon points="71,76 100,68 100,100 67,100" fill="#14923f"/>
  </svg>
  <div class="sign__text sign__lease">LEASE</div>
  <div class="sign__text sign__offer sign__offer--top">Office Space</div>
  <div class="sign__text sign__offer sign__offer--bottom">Available</div>
  <div class="sign__text sign__contact sign__contact--one">Nell Ruby&nbsp; 555-018-3274</div>
  <div class="sign__text sign__contact sign__contact--two">Carl Ivey 555-018-3274</div>
  <div class="sign__text sign__url">www.vantorile.com</div>
  <div class="sign__text sign__brand">Harwell<br>Property<br>Group</div>
</section>
<div class="size-label size-label--wide">8′ x 4′</div>

<section class="sign sign--tall" aria-label="Upright lease sign">
  <svg class="sign__shapes" viewBox="0 0 100 100" preserveAspectRatio="none" aria-hidden="true">
    <defs>
      <linearGradient id="bandTall" x1="0" y1="0" x2="0" y2="1">
        <stop offset="0" stop-color="#6cb52f"/>
        <stop offset="0.65" stop-color="#0f9f45"/>
      </linearGradient>
    </defs>
    <polygon points="86,0 100,0 100,100 60,100" fill="url(#bandTall)"/>
    <polygon points="0,85 66,77 60,100 0,100" fill="#2f7c66"/>
    <polygon points="66,77 100,72 100,100 60,100" fill="#14923f"/>
  </svg>
  <div class="sign__text sign__lease">LEASE</div>
  <div class="sign__text sign__offer sign__offer--top">Office Space</div>
  <div class="sign__text sign__offer sign__offer--bottom">Available</div>
  <div class="sign__text sign__contact sign__contact--one">Nell Ruby&nbsp; 555-018-3274</div>
  <div class="sign__text sign__contact sign__contact--two">Carl Ivey 555-018-3274</div>
  <div class="sign__text sign__url">www.vantorile.com</div>
  <div class="sign__text sign__brand">Harwell<br>Property<br>Group</div>
</section>
<div class="size-label size-label--tall">4′ x 8′</div>

</body>
</html>
```